KTVance Auctions on responsive WP

We need a wordpress design for an established auction and real estate company based in South Carolina. The winning design will incorporate a professional color scheme with company logo in a clean layout. The design needs to consider that this will be developed on a responsive theme. Colors are those that will highlight the logo.

Industry/Entity Type

Real Estate

Font styles to use
Serif
Sans Serif

Colors

Designer to choose colors to be used in the design.

Requirements
Must have
• Colors will be black, dark gray and red. A dark color scheme is ok. They like marlowick.net as a layout. Site tagline - "Auctioneers & Appraisers Since 1977" Site will have slideshow, please use stock photo for the initial image.

- navigation: 1) home 2) Auctions 3) For Sale 4) Buyers & Sellers 5) FAQ 6) About Us 7) Links 8) Contact Us

Widgets - 1) Join Our Email List 2) Social media icons (FB, twitter, RSS) 3) Featured Auctions 4) News & Events blog

footer will have smaller company logo, contact info (below) and attached association logos.
Phone: (803) 555-0147
Contacts: Derek Vance
Email: derek@ktvance-example.com
Address: 482 North Birchfield (Hwy. 61), Ridgeway, SC 29130
Nice to have
• Use and style of a dropmenu - Under AUCTIONS 1) upcoming auctions 2) past auctions

```html
<!DOCTYPE html>
<html lang="en">
<head>
<meta charset="utf-8">
<title>KTVance Auctions</title>
<link rel="stylesheet" href="https://fonts.googleapis.com/css2?family=Cinzel:wght@400;600&family=Roboto:wght@400;500;700&display=swap">
<style>
:root{
  --red:#e31837;
  --slate:#3a4a59;
  --dark:#333536;
  --light:#e9eae9;
  --panel:#efefef;
  --border:#d6d6d6;
  --text:#2b2b2b;
  --green:#6c8a3a;
}
*{margin:0;padding:0;box-sizing:border-box}
html,body{width:998px;height:1200px;overflow:hidden}
body{position:relative;background:#fff;font-family:'Roboto',Arial,sans-serif;color:var(--text)}
.abs{position:absolute}
.serif{font-family:'Cinzel',Georgia,serif}

.header{left:0;top:0;width:998px;height:205px;background:var(--light)}
.brand{left:94px;top:66px;font-family:'Roboto',Arial,sans-serif;font-weight:700;color:var(--slate);font-size:32px;line-height:36px;display:flex;align-items:center;gap:10px;white-space:nowrap}
.brand-mark{width:18px;height:18px;background:var(--red)}
.social{left:722px;top:40px;display:flex;gap:16px}
.social span{width:36px;height:36px;border-radius:50%;display:block}
.tagline{left:412px;top:104px;font-size:22px;color:var(--slate);letter-spacing:.5px;white-space:nowrap}
.tagline b{color:var(--red);font-weight:600}

.nav{left:89px;top:163px;width:818px;height:40px;background:var(--red);border-radius:4px;display:flex}
.nav a{color:#fff;text-decoration:none;font-size:13.5px;font-weight:500;display:flex;align-items:center;justify-content:center;border-right:1px solid #b8132c;height:100%}
.nav a:last-child{border-right:0}
.nav a.active{background:var(--dark)}
.dropdown{left:162px;top:205px;width:152px;z-index:2}
.dropdown a{display:block;height:36px;line-height:36px;padding-left:12px;color:#fff;font-size:12.5px;font-weight:500;text-decoration:none}
.dropdown a:first-child{background:var(--red)}
.dropdown a:last-child{background:var(--dark)}

.band{left:0;top:205px;width:998px;height:294px;background:var(--slate)}
.slide{left:92px;top:220px;width:540px;height:263px;border:2px solid #cfd3d6;background:linear-gradient(180deg,#9dbfd9 0%,#d8d2bf 45%,#5f7a3f 100%)}
.signup{left:653px;top:220px;width:254px;height:263px;background:var(--red);border-radius:3px;color:#fff;overflow:hidden}
.signup h2{position:absolute;left:14px;top:24px;font-size:22px;font-weight:400;white-space:nowrap}
.signup p{position:absolute;left:16px;top:80px;width:224px;font-size:11.3px;line-height:16.5px;hyphens:auto}
.signup .ring{position:absolute;left:140px;top:135px;width:108px;height:108px;border-radius:50%;border:14px solid #cc1430}
.signup .btn{position:absolute;left:54px;top:178px;width:141px;height:39px;background:linear-gradient(#f7f7f7,#d9d9d9);border-radius:4px;color:var(--slate);font-size:19px;font-weight:500;display:flex;align-items:center;justify-content:center;box-shadow:0 2px 3px rgba(0,0,0,.3)}

.welcome h1{position:absolute;left:98px;top:521px;font-size:21px;font-weight:400;color:var(--dark);letter-spacing:.5px;white-space:nowrap}
.welcome p{position:absolute;left:100px;top:557px;width:512px;font-size:12px;line-height:15px}

.card{left:97px;width:523px;height:190px;background:linear-gradient(#fafafa,#e9e9e9);border:1px solid var(--border);border-radius:5px}
.card h3{position:absolute;left:8px;top:6px;width:506px;height:27px;background:var(--slate);color:#fff;font-size:14px;font-weight:500;letter-spacing:.3px;line-height:27px;padding-left:9px}
.card .photo{position:absolute;left:16px;top:44px;width:150px;height:93px;border:2px solid #cfcfcf;background:linear-gradient(180deg,#b8cde0 0%,#9aa98d 45%,#4a4d52 100%)}
.card .info{position:absolute;left:177px;top:44px;width:340px;font-size:11.5px;line-height:15px}
.card .kind{color:var(--red);font-weight:500;font-size:12.3px;margin-bottom:5px}
.card .kind.alt{color:var(--green)}
.card .row{margin-top:8px}
.card .row b{color:var(--slate);font-weight:700}
.card .actions{position:absolute;left:22px;top:149px;display:flex;align-items:center;font-size:12.3px}
.card .actions span{display:flex;align-items:center;gap:5px}
.card .sep{width:1px;height:28px;background:#ccc;margin:0 12px}
.card .bid{position:absolute;left:176px;top:149px;width:224px;height:28px;background:var(--red);border:1px solid #9c1024;border-radius:3px;color:#fff;font-size:11.8px;font-weight:500;display:flex;align-items:center;justify-content:center}

.side{left:655px;width:249px;background:var(--panel);border:1px solid var(--border);border-radius:4px}
.side h2{position:absolute;left:16px;font-size:22px;font-weight:400;color:var(--dark);white-space:nowrap}
.featured .sub{position:absolute;left:17px;top:59px;font-size:11.5px;font-weight:500}
.featured .photo{position:absolute;left:17px;top:72px;width:215px;height:78px;border:2px solid #fff;background:linear-gradient(180deg,#8fb6d8 0%,#c9c4b6 50%,#5e7a45 100%)}
.featured .meta{position:absolute;left:17px;top:166px;width:188px;font-size:10.5px;line-height:13.5px}
.featured .meta p+p{margin-top:7px}
.news .item{position:absolute;left:17px;width:205px;font-size:11px;line-height:15px;letter-spacing:.2px}

.footer{left:0;top:1062px;width:998px;height:138px;background:var(--slate);color:#fff}
.footer h2{position:absolute;left:101px;top:18px;font-size:16px;font-weight:400;letter-spacing:.5px;white-space:nowrap}
.footer ul{position:absolute;left:101px;top:48px;list-style:none;font-size:11.5px;line-height:18.5px}
.badges{position:absolute;left:472px;top:30px;display:flex;gap:14px;align-items:center}
.badges span{display:block;background:#dfe3e6}
.footer .mini-brand{position:absolute;left:778px;top:33px;font-family:'Roboto',Arial,sans-serif;font-weight:700;font-size:18px;line-height:20px;color:#fff;display:flex;align-items:center;gap:7px;white-space:nowrap}
.footer .mini-brand i{width:10px;height:10px;background:var(--red);display:block}
.copyright{position:absolute;left:471px;top:100px;font-size:11.2px;white-space:nowrap}
</style>
</head>
<body>

<header class="abs header">
  <div class="abs brand"><span class="brand-mark"></span><span>KTVance Auctions</span></div>
  <div class="abs social">
    <span style="background:#3c5a99" role="img" aria-label="Social profile link"></span>
    <span style="background:#3fb4ec" role="img" aria-label="Social updates link"></span>
    <span style="background:#f7891f" role="img" aria-label="News feed link"></span>
  </div>
  <div class="abs tagline serif">AUCTIONEERS &amp; APPRAISERS <b>SINCE 1977</b></div>
</header>

<nav class="abs nav">
  <a style="width:75px">HOME</a>
  <a class="active" style="width:130px">AUCTIONS</a>
  <a style="width:104px">FOR SALE</a>
  <a style="width:156px">BUYERS &amp; SELLER</a>
  <a style="width:80px">FAQ</a>
  <a style="width:95px">ABOUT US</a>
  <a style="width:72px">LINKS</a>
  <a style="width:106px">CONTACT US</a>
</nav>

<section class="abs band"></section>
<div class="abs slide" role="img" aria-label="Slideshow: two-storey family home with porch and trees"></div>
<div class="abs dropdown">
  <a>UPCOMING AUCTIONS</a>
  <a>PAST AUCTIONS</a>
</div>
<aside class="abs signup">
  <h2 class="serif">JOIN OUR EMAI LIST</h2>
  <p>Please join our free mailing list to get auction alerts and news for upcoming events. Simply enter your email address below:</p>
  <div class="ring"></div>
  <div class="btn">Join Now</div>
</aside>

<section class="welcome">
  <h1 class="serif">WELCOME TO KTVANCE AUCTIONEERS INC</h1>
  <p>K. T. Vance &amp; Co., Auctioneers, has been in business since 1977. We are a Full Time - Full Service auction company, conducting estate auctions, bankruptcies, liquidations, equipment, real estate and horse auctions</p>
</section>

<article class="abs card" style="top:625px">
  <h3>Absolute Auction - Home &amp; 32 Acres</h3>
  <div class="photo" role="img" aria-label="Crowd gathered in front of a house for an auction"></div>
  <div class="info">
    <div class="kind">LIVE ON-SITE AUCTION</div>
    <div>Harlow BS3F High Lift, 600 Series Brennan tractor w/Halden Loader, Dune buggy, 1207 KR Cutditioner: SHOP &amp;</div>
    <div class="row"><b>Begins:</b>&nbsp; Saturday, March 16, 2013 at 10:00 AM EDT</div>
    <div class="row"><b>Location:</b>&nbsp; 7290 Marren Road Glenfield, KY 40099</div>
  </div>
  <div class="actions">
    <span><svg width="12" height="12" viewBox="0 0 12 12"><circle cx="5" cy="5" r="3.8" fill="none" stroke="#222" stroke-width="1.8"/><line x1="8" y1="8" x2="11" y2="11" stroke="#222" stroke-width="2"/></svg>Details</span>
    <i class="sep"></i>
    <span><svg width="16" height="12" viewBox="0 0 16 12"><rect x=".5" y=".5" width="15" height="11" fill="#fff" stroke="#444"/><path d="M2 10l4-5 3 3 2-2 3 4z" fill="#555"/></svg>Gallery</span>
  </div>
  <div class="bid">Click here for our online Bidding site</div>
</article>

<article class="abs card" style="top:841px">
  <h3>Absolute Auction - Home &amp; 32 Acres</h3>
  <div class="photo" role="img" aria-label="Crowd gathered in front of a house for an auction"></div>
  <div class="info">
    <div class="kind alt">LIVE ON-SITE AUCTION</div>
    <div>Harlow BS3F High Lift, 600 Series Brennan tractor w/Halden Loader, Dune buggy, 1207 KR Cutditioner: SHOP &amp;</div>
    <div class="row"><b>Begins:</b>&nbsp; Saturday, March 16, 2013 at 10:00 AM EDT</div>
    <div class="row"><b>Location:</b>&nbsp; 7290 Marren Road Glenfield, KY 40099</div>
  </div>
  <div class="actions">
    <span><svg width="12" height="12" viewBox="0 0 12 12"><circle cx="5" cy="5" r="3.8" fill="none" stroke="#222" stroke-width="1.8"/><line x1="8" y1="8" x2="11" y2="11" stroke="#222" stroke-width="2"/></svg>Details</span>
    <i class="sep"></i>
    <span><svg width="16" height="12" viewBox="0 0 16 12"><rect x=".5" y=".5" width="15" height="11" fill="#fff" stroke="#444"/><path d="M2 10l4-5 3 3 2-2 3 4z" fill="#555"/></svg>Gallery</span>
  </div>
  <div class="bid">Click here for our online Bidding site</div>
</article>

<aside class="abs side featured" style="top:521px;height:228px">
  <h2 class="serif" style="top:12px">FEATURED AUCTION</h2>
  <div class="sub">Multi Estate &amp; Consignment Auction</div>
  <div class="photo" role="img" aria-label="Agent in a suit standing before a suburban house"></div>
  <div class="meta">
    <p><b>Start Date/ Time:</b> Saturday, April 13, 2013 At 10:00 Am</p>
    <p><b>Location:</b> 3150 New Castleford,&nbsp; 73899</p>
  </div>
</aside>

<aside class="abs side news" style="top:778px;height:253px">
  <h2 class="serif" style="top:14px">NEWS BLOG</h2>
  <p class="item" style="top:52px">Harlow BS3F High Lift, 6Series Brennan tractor Harlow BS3F High Lift, 6Series</p>
  <p class="item" style="top:104px">Harlow BS3F High Lift, 6Series Brennan tractor Harlow BS3F High Lift, 6Series</p>
  <p class="item" style="top:158px">Harlow BS3F High Lift, 6Series Brennan tractor Harlow BS3F High Lift, 6Series</p>
</aside>

<footer class="abs footer">
  <h2 class="serif">KTVANCE AUCTIONEERS AUCTION</h2>
  <ul>
    <li>Phone: (803) 555-0147</li>
    <li>Contacts: Derek Vance</li>
    <li>Email: derek@ktvance-example.com</li>
    <li>Address: 482 North Birchfield (Hwy. 61), Ridgewell, SC 29199</li>
  </ul>
  <div class="badges">
    <span style="width:112px;height:32px;border-radius:3px" role="img" aria-label="State association badge"></span>
    <span style="width:42px;height:46px;border-radius:3px" role="img" aria-label="National association badge"></span>
    <span style="width:56px;height:46px;border-radius:50%" role="img" aria-label="Certification badge"></span>
  </div>
  <div class="mini-brand"><i></i><span>KTVance Auctions</span></div>
  <div class="copyright">Copyright © 2007 - 2014 - K. T. Vance &amp; Company Auctioneers - All Rights Reserved</div>
</footer>

</body>
</html>
```